RAVEL ELECTRICAL GROUP Website Providing Electrical Services

We're a company providing electrical services to the public. We're located in Bankstown a suburb in Sydney, Australia. We are a team of 4 electricians that provide service work to the public. We work on new construction buildings such as single story, double story & units. We also do office fit outs & commercial factory work.

Target Market(s)

All Age Groups
Construction People
Sydney, Australia

Industry/Entity Type

Electrical

Contact Information for Business Card

Name Martin Fells
Contact Number 0412 583 074
Company License 574093B
ABN 54 203 817 465
Residential Commercial Industrial
info@ravelelectrical.example.au

Coding

Coded - Design and coding required

Number of Pages Required

5+ page

Font styles to use
Serif
Sans Serif

Colors

Designer to choose colors to be used in the design.

Requirements
Must have
• WORDPRESS
• Nice & Simple
• Eye catching
• Easy to Read
• Contact details
• Instagram Linked
• Facebook Page Linked
• All Social Media Linked
• Live Chat
• Form Submission
• Testimonial
• Specify services Offered
• About Us (Company details)
• Industrial Installation Page
• Residential Installation Page
• Commercial Installation Page
• Mode of payment (cash, credit-debit card, cheque)
• Local & national electrical news
• Project Videos
• Newsletter
• Level 2 licensed accredited
• Project pictures and articles
• Awards
• Legalities (company's policy, terms, rules)
• FAQ's (Frequently asked questions)
• Collaboration Projects
• Careers
• Projects
• Suppliers
• Customer Perks (discounts or freebies)
• Employees Informations (pictures and basic information)
• Opening Hours and Map location
• Company Logo & Company License (owner license)
• Accreditation
• Customer Service
• Safety/Safety tips
• Clients information (regular clients)
• Expertise
• Company's processes
• Timeline page
• Homepage
• Specify installations
• Search toolbar
• Portfolio
• Request for an appointment - servicing
• Feedbacks
Nice to have
• Articles (better if recent project articles)
• Advertisement
• Influencer Quote
• Sneak Peeks (if you have new services offered)
• Staff Highlights
• Job Hiring (Career Growth)
• Ratings (Rate our service)
• A day/week in the work
• Personal Anecdotes
• Before and after post projects
• Ecological Values
• Marketing feature
• Tagline
• Streaming interactive videos
• Timeline
• Calendar
• Blog
• Emergency Services/Hotline
• Additional services offered
• Transportation (vehicle - car images of our company)
• Comment box (company - clients)
• Rate Us (Performance rating)
Should not have
• Website shouldn't be dark
• Website shouldn't be hard to read
• Advertisement of competitors
• Moving objects
• Dark background

```html
<!DOCTYPE html>
<html lang="en">
<head>
<meta charset="utf-8">
<title>Ravel Electrical Group – Home</title>
<link rel="stylesheet" href="https://fonts.googleapis.com/css2?family=Poppins:wght@300;400;500;600;700&family=Open+Sans:wght@400;600&display=swap">
<style>
:root{
  --blue:#1a7fcc;
  --blue-dark:#1466a8;
  --ink:#222a33;
  --muted:#6b7480;
  --light:#f0f1f3;
  --card:#e9eaec;
  --white:#ffffff;
  --footer:#1f252c;
  --footer-line:#323a43;
  --hero-a:#0b1c33;
  --hero-b:#1d3f6b;
}
*{box-sizing:border-box;margin:0;padding:0}
html,body{width:1200px;height:2840px;overflow:hidden}
body{font-family:"Open Sans",Arial,sans-serif;color:var(--ink);background:var(--white);position:relative}
.heading{font-family:"Poppins",Arial,sans-serif}
a{color:inherit;text-decoration:none}

/* header */
.site-header{position:absolute;top:0;left:0;width:1200px;height:120px;background:var(--white)}
.brand{position:absolute;left:80px;top:26px;display:flex;align-items:center;gap:12px}
.brand-mark{width:40px;height:40px;border-radius:50%;background:var(--blue)}
.brand-name{font-family:"Poppins",sans-serif;font-weight:600;font-size:17px;color:var(--blue);letter-spacing:1px;line-height:1.15;width:130px}
.top-bar{position:absolute;right:80px;top:22px;display:flex;align-items:center;gap:28px;font-family:"Poppins",sans-serif;font-size:13px;color:var(--ink)}
.top-bar .account{display:flex;gap:10px;align-items:center}
.social-dots{display:flex;gap:8px}
.social-dots span{width:22px;height:22px;border-radius:50%;background:var(--blue)}
.main-nav{position:absolute;right:80px;top:80px;display:flex;gap:42px;font-family:"Poppins",sans-serif;font-size:14px;font-weight:500;color:var(--ink)}

/* hero */
.hero{position:absolute;top:120px;left:0;width:1200px;height:652px;overflow:hidden}
.hero-photo{position:absolute;inset:0;background:radial-gradient(circle at 70% 30%,#7bb4e8 0%,#2c5d93 22%,var(--hero-b) 45%,var(--hero-a) 100%)}
.hero-text{position:absolute;left:88px;top:168px;color:var(--white)}
.hero-text .line1,.hero-text .line2{font-family:"Poppins",sans-serif;font-weight:600;font-size:56px;letter-spacing:3px;line-height:1.3}
.hero-text .tagline{font-family:"Poppins",sans-serif;font-size:30px;font-weight:400;letter-spacing:3px;margin-top:14px;padding-bottom:14px;border-bottom:2px solid var(--white);display:inline-block;width:420px}
.hero-actions{display:flex;gap:26px;margin-top:42px}
.btn{display:inline-block;background:var(--blue);color:var(--white);font-family:"Poppins",sans-serif;font-weight:600;font-size:16px;letter-spacing:1px;padding:18px 34px;text-transform:uppercase}

/* testimonial + schedule */
.testimonial{position:absolute;top:800px;left:0;width:612px;height:328px;background:var(--light)}
.quote-mark{position:absolute;left:76px;top:30px;font-family:"Poppins",serif;font-size:90px;color:#c6cace;line-height:1}
.quote-text{position:absolute;left:82px;top:90px;width:260px;font-size:17px;line-height:1.6;color:var(--ink)}
.quote-name{position:absolute;left:82px;top:240px;font-family:"Poppins",sans-serif;font-size:20px;font-weight:500}
.quote-role{position:absolute;left:82px;top:272px;font-family:"Poppins",sans-serif;font-size:18px;color:var(--blue)}
.quote-photo{position:absolute;left:352px;top:36px;width:230px;height:250px;background:linear-gradient(160deg,#d9d4cf,#a99b90)}
.schedule{position:absolute;top:800px;left:612px;width:588px;height:328px;background:var(--blue)}
.schedule h2{position:absolute;left:56px;top:34px;font-family:"Poppins",sans-serif;font-weight:500;font-size:30px;color:var(--white)}
.schedule .rule{position:absolute;left:56px;top:82px;width:300px;height:2px;background:rgba(255,255,255,.6)}
.form-grid{position:absolute;left:56px;top:104px;width:490px;display:grid;grid-template-columns:repeat(3,1fr);gap:18px 14px}
.field{height:48px;background:var(--blue-dark);border:1px solid rgba(255,255,255,.35);color:#d6e6f5;font-size:13px;padding:0 14px;display:flex;align-items:center;justify-content:space-between}
.submit{grid-column:1/4;height:44px;background:#0f4f85;color:var(--white);font-family:"Poppins",sans-serif;font-size:16px;display:flex;align-items:center;justify-content:center}

/* services */
.services-title{position:absolute;top:1190px;left:0;width:1200px;text-align:center;font-family:"Poppins",sans-serif;font-weight:500;font-size:44px;letter-spacing:1px}
.title-rule{position:absolute;top:1258px;left:520px;width:160px;height:20px}
.service-card{position:absolute;top:1300px;width:324px;height:232px;background:var(--card);padding:26px 24px}
.service-icon{width:58px;height:58px;border-radius:50%;background:var(--blue);display:flex;align-items:center;justify-content:center;float:left}
.service-card h3{margin-left:86px;font-family:"Poppins",sans-serif;font-weight:400;font-size:23px;line-height:1.3;min-height:70px}
.service-card p{clear:both;margin-top:22px;font-size:13px;color:var(--muted);line-height:1.6}
.service-card .more{display:block;margin-top:12px;font-size:13px;color:var(--blue)}
.slide-arrow{position:absolute;top:1390px;width:34px;height:34px;border-radius:50%;background:#dcdee1;display:flex;align-items:center;justify-content:center}
.view-all{position:absolute;top:1572px;left:504px;width:192px;height:58px;background:var(--blue);color:var(--white);font-family:"Poppins",sans-serif;font-weight:500;font-size:18px;display:flex;align-items:center;justify-content:center}

/* project gallery */
.gallery{position:absolute;top:1672px;left:80px;width:1032px;display:grid;grid-template-columns:repeat(4,240px);grid-auto-rows:174px;gap:24px 24px}
.gallery div{box-shadow:0 0 0 6px #ececec}

/* about */
.about{position:absolute;top:2100px;left:0;width:1200px;height:332px;background:var(--light)}
.about-photo{position:absolute;left:0;top:0;width:592px;height:332px;background:linear-gradient(135deg,#e9e6df,#b8b2a6 60%,#8f8a80)}
.about-body{position:absolute;left:660px;top:44px;width:440px}
.about-body h2{font-family:"Poppins",sans-serif;font-weight:500;font-size:40px;letter-spacing:1px}
.about-body .rule{width:90px;height:3px;background:var(--blue);margin:8px 0 18px}
.about-body p{font-size:14px;line-height:1.7;color:var(--muted)}
.about-body .btn-small{display:inline-block;margin-top:22px;background:var(--blue);color:var(--white);font-family:"Poppins",sans-serif;font-size:13px;font-weight:600;padding:12px 26px}

/* footer */
.site-footer{position:absolute;top:2432px;left:0;width:1200px;height:408px;background:var(--footer);color:#aab2bb}
.footer-brand{position:absolute;left:188px;top:56px;display:flex;flex-direction:column;align-items:flex-start;gap:8px}
.footer-brand .box{width:100px;height:74px;background:var(--white);display:flex;align-items:center;justify-content:center;padding:6px}
.footer-brand .box span{font-family:"Poppins",sans-serif;font-weight:600;font-size:12px;color:var(--blue);text-align:center;line-height:1.2}
.footer-about{position:absolute;left:188px;top:150px;width:230px;font-size:13px;line-height:1.6}
.footer-contact{position:absolute;left:160px;top:236px;font-size:13px;line-height:2.2}
.footer-contact div{display:flex;align-items:center;gap:14px}
.footer-col-title{font-family:"Poppins",sans-serif;font-size:14px;font-weight:500;color:var(--white);letter-spacing:1px;text-transform:uppercase}
.recent{position:absolute;left:500px;top:56px;width:300px}
.post{padding:18px 0;border-bottom:1px solid var(--footer-line)}
.post h4{font-family:"Poppins",sans-serif;font-weight:500;font-size:14px;color:var(--white)}
.post .date{font-size:12px;color:var(--muted);margin:6px 0}
.post p{font-size:12px;line-height:1.5}
.newsletter{position:absolute;left:880px;top:56px;width:220px}
.signup{display:flex;margin-top:22px}
.signup .input{flex:1;height:38px;border:1px solid #49525c;font-size:12px;padding:0 10px;display:flex;align-items:center}
.signup .go{width:44px;height:38px;background:var(--blue);color:var(--white);font-family:"Poppins",sans-serif;font-size:13px;display:flex;align-items:center;justify-content:center}
.follow{margin-top:34px}
.follow-dots{display:flex;gap:26px;margin-top:18px}
.follow-dots span{width:18px;height:18px;border-radius:50%;background:#cfd5db}
.copyright{position:absolute;left:0;bottom:0;width:1200px;height:48px;border-top:1px solid var(--footer-line);text-align:center;font-size:12px;line-height:48px;color:var(--muted)}
</style>
</head>
<body>

<header class="site-header">
  <a class="brand" href="#"><span class="brand-mark"></span><span class="brand-name">RAVEL ELECTRICAL GROUP</span></a>
  <div class="top-bar">
    <div class="account">
      <svg width="14" height="14" viewBox="0 0 14 14"><circle cx="7" cy="4.5" r="3" fill="#1a7fcc"/><path d="M1 13c0-3.5 2.7-5 6-5s6 1.5 6 5z" fill="#1a7fcc"/></svg>
      <span>LOGIN</span><span>|</span><span>REGISTER</span>
    </div>
    <div class="social-dots"><span></span><span></span><span></span></div>
  </div>
  <nav class="main-nav">
    <a href="#">HOME</a><a href="#">ABOUT US</a><a href="#">OUR SERVICES</a><a href="#">PROJECTS</a><a href="#">NEWS</a><a href="#">CONTACT US</a>
  </nav>
</header>

<section class="hero">
  <div class="hero-photo" role="img" aria-label="Electrician in a hard hat reaching up to a glowing spark of electricity against a night city backdrop"></div>
  <div class="hero-text">
    <div class="line1">WE'RE THE</div>
    <div class="line2">CURRENT SPECIALIST</div>
    <div class="tagline">KEEPING YOU WIRED</div>
    <div class="hero-actions"><a class="btn" href="#">Know More</a><a class="btn" href="#">Contact Us</a></div>
  </div>
</section>

<section class="testimonial">
  <div class="quote-mark">“</div>
  <p class="quote-text">It is a long established fact that a reader will be distracted by the readable content of a page when looking at its layout.</p>
  <div class="quote-name">Daniel Reeve,</div>
  <div class="quote-role">Businessman</div>
  <div class="quote-photo" role="img" aria-label="Smiling couple, satisfied customers"></div>
</section>

<section class="schedule">
  <h2>Schedule Services</h2>
  <div class="rule"></div>
  <div class="form-grid">
    <div class="field">Name...</div>
    <div class="field">Email Id...</div>
    <div class="field">Date...</div>
    <div class="field">Phone No...</div>
    <div class="field">Suburb...</div>
    <div class="field">Electrical Installation <svg width="10" height="6" viewBox="0 0 10 6"><path d="M0 0l5 6 5-6z" fill="#d6e6f5"/></svg></div>
    <div class="submit">Submit</div>
  </div>
</section>

<h2 class="services-title">OUR SERVICES</h2>
<svg class="title-rule" viewBox="0 0 160 20"><line x1="0" y1="10" x2="66" y2="10" stroke="#1a7fcc" stroke-width="2"/><line x1="94" y1="10" x2="160" y2="10" stroke="#1a7fcc" stroke-width="2"/><path d="M82 1l-8 10h6l-3 8 9-11h-6z" fill="#1a7fcc"/></svg>

<div class="slide-arrow" style="left:26px"><svg width="10" height="12" viewBox="0 0 10 12"><path d="M8 1L2 6l6 5" stroke="#777" stroke-width="2" fill="none"/></svg></div>
<div class="slide-arrow" style="left:1140px"><svg width="10" height="12" viewBox="0 0 10 12"><path d="M2 1l6 5-6 5" stroke="#777" stroke-width="2" fill="none"/></svg></div>

<article class="service-card" style="left:88px">
  <div class="service-icon"><svg width="28" height="28" viewBox="0 0 28 28"><path d="M16 2L6 16h7l-2 10 11-15h-7z" fill="#fff"/></svg></div>
  <h3>Electrical Maintenance</h3>
  <p>The first mate and his Skipper too will do their very best to help.</p>
  <a class="more" href="#">Read More...</a>
</article>
<article class="service-card" style="left:440px">
  <div class="service-icon"><svg width="28" height="28" viewBox="0 0 28 28"><circle cx="14" cy="11" r="7" fill="#fff"/><rect x="10" y="19" width="8" height="6" fill="#fff"/></svg></div>
  <h3>Lightings &amp; Repair</h3>
  <p>The first mate and his Skipper too will do their very best to help.</p>
  <a class="more" href="#">Read More...</a>
</article>
<article class="service-card" style="left:788px">
  <div class="service-icon"><svg width="28" height="28" viewBox="0 0 28 28"><path d="M6 14l6 6 11-12" stroke="#fff" stroke-width="3" fill="none"/></svg></div>
  <h3>Installation</h3>
  <p>The first mate and his Skipper too will do their very best to help.</p>
  <a class="more" href="#">Read More...</a>
</article>

<a class="view-all" href="#">VIEW ALL</a>

<section class="gallery">
  <div role="img" aria-label="Coils of electrical cable" style="background:linear-gradient(135deg,#d9c6b4,#a26b4a)"></div>
  <div role="img" aria-label="Colourful wiring in a switchboard" style="background:linear-gradient(135deg,#c94a3a,#4a5c7a)"></div>
  <div role="img" aria-label="Electrician working on a ceiling fitting" style="background:linear-gradient(135deg,#e8d27a,#6a6f78)"></div>
  <div role="img" aria-label="Multimeter testing a circuit" style="background:linear-gradient(135deg,#5b6470,#d8b23c)"></div>
  <div role="img" aria-label="Electrician installing a switchboard" style="background:linear-gradient(135deg,#8ba0b8,#3b4a5c)"></div>
  <div role="img" aria-label="Sparks from electrical work" style="background:linear-gradient(135deg,#2b2420,#c9782c)"></div>
  <div role="img" aria-label="Industrial electrical panel" style="background:linear-gradient(135deg,#b7bcc2,#6e757d)"></div>
  <div role="img" aria-label="Electrical plans with tools" style="background:linear-gradient(135deg,#f0f0ee,#9aa3ad)"></div>
</section>

<section class="about">
  <div class="about-photo" role="img" aria-label="Pliers, cutters and cables on a workbench"></div>
  <div class="about-body">
    <h2>ABOUT US</h2>
    <div class="rule"></div>
    <p>Ravel Electrical is a family owned and operated full service electrical repair, installation and parts supply team. Save time and money compared with other contractors. Contact us today to get your home or site up and working again in no time at all.</p>
    <a class="btn-small" href="#">LEARN MORE</a>
  </div>
</section>

<footer class="site-footer">
  <div class="footer-brand"><div class="box"><span>RAVEL ELECTRICAL GROUP</span></div></div>
  <p class="footer-about">Lorem ipsum is simply dummy text of the printing and typesetting industry.</p>
  <div class="footer-contact">
    <div><svg width="14" height="14" viewBox="0 0 14 14"><path d="M3 1l3 3-2 2c1 2 2 3 4 4l2-2 3 3-2 2C6 13 1 8 1 3z" fill="#1a7fcc"/></svg>0412 583 074</div>
    <div><svg width="14" height="12" viewBox="0 0 14 12"><rect x="0.5" y="0.5" width="13" height="11" fill="none" stroke="#1a7fcc"/><path d="M1 1l6 5 6-5" stroke="#1a7fcc" fill="none"/></svg>info@ravelelectrical.example.au</div>
  </div>

  <div class="recent">
    <div class="footer-col-title">Recent Posts</div>
    <div class="post">
      <h4>Nulla consequat massa quis enim</h4>
      <div class="date">November 15, 2018</div>
      <p>The right of passage when wiring new homes is a safe switchboard.</p>
    </div>
    <div class="post">
      <h4>Nulla consequat massa quis enim</h4>
      <div class="date">November 15, 2018</div>
      <p>The right of passage when wiring new homes is a safe switchboard.</p>
    </div>
  </div>

  <div class="newsletter">
    <div class="footer-col-title">Newsletter</div>
    <div class="signup"><div class="input">Email Address</div><div class="go">GO</div></div>
    <div class="follow">
      <div class="footer-col-title">Follow Us</div>
      <div class="follow-dots"><span></span><span></span><span></span><span></span></div>
    </div>
  </div>

  <div class="copyright">Copyright © 2018 Ravel Electrical Group. All rights reserved.</div>
</footer>

</body>
</html>
```